Website Design for Dealership
Need Website Designer- examples provided
I have given feedback- please submit any requested changes, we are looking to choose our winner by tomorrow afternoon.
Why did the contest get extended? Any feedback on the designs?
RT/KWF/NJ Team
Dear QD,
Kindly upload Logos and photos as mentioned by you so that we can start working on this project.
thanks
quillforge
I have 2 Adobe Illustrator files of the logos we are to use on the website. The red oval one is the Manufacturer. The ‘Haulwright of NYC’ is our specific location. I also have 8 .jpegs of trucks you can use on the site.
Lastly-
We really want the website to model the Atlanta Haulwright website example we provided. The only differences are- we do not have a body shop. The tabs/categories that should be displayed on the website are:
“Home/Truck Sales/Service/Parts/About Us”

```html
<!DOCTYPE html>
<html lang="en">
<head>
<meta charset="utf-8">
<title>Haulwright of Farmingdale</title>
<link href="https://fonts.googleapis.com/css2?family=PT+Sans:wght@400;700&family=Open+Sans:wght@300;400&display=swap" rel="stylesheet">
<style>
  :root {
    --red: #a3141c;
    --red-dark: #6e0c10;
    --red-light: #c8252d;
    --grey-top: #e4e4e4;
    --grey-nav: #d3d3d3;
    --text: #6b6b6b;
    --text-dark: #333;
    --footer: #4a4a4a;
    --footer-dark: #3b3b3b;
    --footer-text: #d8d8d8;
    --white: #fff;
  }
  * { box-sizing: border-box; margin: 0; padding: 0; }
  html, body { width: 1200px; height: 988px; overflow: hidden; }
  body {
    position: relative;
    font-family: "PT Sans", sans-serif;
    color: var(--text);
    background: var(--white);
  }
  .top-band {
    position: absolute; left: 0; top: 0; width: 1200px; height: 378px;
    background: linear-gradient(#f2f2f2, var(--grey-top));
    border-bottom: 1px solid #d6d6d6;
  }
  .brand-bar {
    position: absolute; left: 94px; top: 21px; width: 1012px; height: 59px;
    border-radius: 30px;
    background: linear-gradient(var(--red-light), var(--red) 50%, var(--red-dark));
    box-shadow: 0 2px 4px rgba(0,0,0,.25);
  }
  .brand-name {
    position: absolute; left: 500px; top: 28px; height: 46px;
    display: flex; align-items: center; gap: 12px;
    color: var(--white); font-size: 32px; font-weight: 700;
  }
  .brand-mark {
    width: 20px; height: 20px; border-radius: 50%; background: var(--white);
  }
  .search {
    position: absolute; left: 943px; top: 37px; width: 142px; height: 27px;
    border-radius: 14px; background: var(--white);
    font-size: 13px; color: #aaa; padding: 5px 12px;
  }
  .search svg { position: absolute; right: 10px; top: 7px; }
  .slider {
    position: absolute; left: 94px; top: 102px; width: 720px; height: 190px;
    background: var(--white);
    border: 3px solid var(--red);
    border-radius: 28px 0 0 28px;
    box-shadow: 0 2px 5px rgba(0,0,0,.2);
  }
  .slider-title {
    position: absolute; left: 32px; top: 50px;
    font-family: "Open Sans", sans-serif; font-weight: 300;
    font-size: 31px; color: var(--red); line-height: 1.1;
  }
  .slider-sub {
    position: absolute; left: 32px; top: 88px;
    font-family: "Open Sans", sans-serif; font-size: 28px; color: #555;
  }
  .slider-art {
    position: absolute; left: 230px; top: 14px; width: 430px; height: 160px;
    background: radial-gradient(ellipse at center, #cfcfcf, #f4f4f4 70%, #fff);
  }
  .slider-dots { position: absolute; left: 36px; top: 158px; display: flex; gap: 9px; }
  .slider-dots span { width: 12px; height: 12px; border-radius: 50%; background: #999; }
  .slider-dots span:first-child { background: var(--red); }
  .hero-truck {
    position: absolute; left: 750px; top: 102px; width: 360px; height: 246px;
    border-radius: 40px 0 30px 30px;
    background: linear-gradient(160deg, #d33a3a, #9c1218 55%, #3a3a3a);
    clip-path: polygon(0 0, 76% 0, 76% 30%, 100% 30%, 100% 100%, 0 100%);
  }
  .dealer-tag {
    position: absolute; left: 1026px; top: 108px; width: 86px;
    color: var(--red); font-weight: 700; font-size: 11px; line-height: 1.2;
    text-align: center; text-transform: uppercase;
  }
  .main-nav {
    position: absolute; left: 94px; top: 303px; width: 710px; height: 52px;
    background: linear-gradient(#e2e2e2, var(--grey-nav));
    border-radius: 0 0 0 24px;
    display: flex; align-items: center; padding-left: 8px;
    box-shadow: 0 2px 3px rgba(0,0,0,.15);
  }
  .main-nav a {
    text-decoration: none; color: #444; font-size: 17px;
    padding: 13px 18px; line-height: 1;
    border-right: 1px solid #bdbdbd;
  }
  .main-nav a:last-child { border-right: 0; }
  .main-nav a.active { background: var(--white); color: var(--red); border-radius: 4px 4px 0 0; }
  h2 {
    position: absolute; font-weight: 400; font-size: 30px; color: var(--red);
  }
  p { font-size: 13.5px; line-height: 1.6; }
  .welcome-title { left: 88px; top: 405px; }
  .welcome-text { position: absolute; left: 88px; top: 456px; width: 680px; }
  .welcome-photo {
    position: absolute; left: 793px; top: 420px; width: 312px; height: 153px;
    border: 4px solid #e6e6e6; border-radius: 6px;
    background: linear-gradient(#2c4f9c, #6a86c7 45%, #c9b64a 70%, #4a4a3a);
  }
  .col-title { top: 645px; }
  .rule { position: absolute; top: 692px; height: 0; border-top: 2px dotted #bbb; }
  .services {
    position: absolute; left: 88px; top: 712px; width: 275px;
    display: flex; flex-direction: column; align-items: flex-start; gap: 12px;
  }
  .services p { font-size: 12.5px; line-height: 1.55; }
  .btn-more {
    width: 100px; height: 26px;
    border-radius: 13px; background: var(--text-dark); color: var(--white);
    font-size: 13px; font-weight: 700; text-align: center; line-height: 26px;
  }
  .trucks-photo {
    position: absolute; left: 445px; top: 718px; width: 300px; height: 134px;
    border: 4px solid #e6e6e6; border-radius: 6px;
    background: linear-gradient(#dfe6ee, #f4f6f8 55%, #b9bec5);
  }
  .news { position: absolute; left: 798px; top: 716px; width: 310px; list-style: none; }
  .news li { position: relative; padding-left: 22px; margin-bottom: 18px; }
  .news li::before {
    content: ""; position: absolute; left: 4px; top: 8px;
    width: 6px; height: 6px; border-radius: 50%; background: var(--red);
  }
  .news time { display: block; font-size: 12px; color: #999; margin-top: 6px; }
  .site-footer {
    position: absolute; left: 0; top: 903px; width: 1200px; height: 85px;
    background: linear-gradient(var(--footer), var(--footer-dark));
    color: var(--footer-text);
  }
  .footer-nav { position: absolute; left: 88px; top: 16px; font-size: 14px; }
  .footer-nav a { color: var(--footer-text); text-decoration: none; }
  .footer-nav span { margin: 0 8px; }
  .copyright { position: absolute; left: 88px; top: 48px; font-size: 14px; }
  .social-badge {
    position: absolute; left: 1008px; top: 26px; width: 102px; height: 30px;
    background: #3a5a98; border: 2px solid #e6e6e6; border-radius: 3px;
  }
</style>
</head>
<body>
  <div class="top-band"></div>

  <header>
    <div class="brand-bar"></div>
    <div class="brand-name"><span class="brand-mark"></span>Haulwright of Farmingdale</div>
    <div class="search">Search
      <svg width="12" height="12" viewBox="0 0 12 12"><circle cx="5" cy="5" r="3.5" fill="none" stroke="#888" stroke-width="1.5"/><line x1="7.5" y1="7.5" x2="11" y2="11" stroke="#888" stroke-width="1.5"/></svg>
    </div>
  </header>

  <section class="slider">
    <div class="slider-art" role="img" aria-label="Faded grey line-up of three haul trucks"></div>
    <div class="slider-title">Cumque nihil impedit</div>
    <div class="slider-sub">MINUS IDQUOD</div>
    <div class="slider-dots"><span></span><span></span><span></span><span></span></div>
  </section>
  <div class="hero-truck" role="img" aria-label="Red haul truck cab seen from the front side"></div>
  <div class="dealer-tag">New York Metro Haulwright, Inc.</div>

  <nav class="main-nav">
    <a class="active" href="#">Home</a>
    <a href="#">Trucks</a>
    <a href="#">Services</a>
    <a href="#">Parts</a>
    <a href="#">About us</a>
    <a href="#">Contact us</a>
    <a href="#">Help</a>
  </nav>

  <main>
    <h2 class="welcome-title">Welcome to our site</h2>
    <p class="welcome-text">Sed ut perspiciatis unde omnis iste natus error sit voluptatem accusantium doloremque laudantium, totam rem aperiam, eaque ipsa quae ab illo inventore veritatis et quasi architecto beatae vitae dicta sunt explicabo. Nemo enim ipsam voluptatem quia voluptas sit aspernatur aut odit aut fugit, sed quia consequuntur magni dolores eos qui ratione voluptatem sequi nesciunt. Neque porro quisquam est, qui dolorem ipsum quia dolor sit amet, consectetur, adipisci velit, sed quia non numquam eius modi tempora incidunt ut labore et dolore magnam aliquam quaerat voluptatem. Ut enim ad minima veniam, quis nostrum exercitationem ullam corporis suscipit laboriosam.</p>
    <div class="welcome-photo" role="img" aria-label="Row of colourful trucks under a blue evening sky"></div>

    <h2 class="col-title" style="left:88px">Our services</h2>
    <h2 class="col-title" style="left:445px">Trucks</h2>
    <h2 class="col-title" style="left:798px">Latest News</h2>
    <div class="rule" style="left:88px;width:270px"></div>
    <div class="rule" style="left:445px;width:300px"></div>
    <div class="rule" style="left:798px;width:310px"></div>

    <div class="services">
      <p>At vero eos et accusamus et iusto odio dignissimos ducimus qui blanditiis praesentium voluptatum deleniti atque corrupti quos dolores et quas molestias excepturi sint occaecati cupiditate non provident, similique sunt in culpa qui officia deserunt mollitia animi.</p>
      <div class="btn-more">VIEW MORE</div>
    </div>

    <div class="trucks-photo" role="img" aria-label="Red haul truck parked on a snowy lot"></div>

    <ul class="news">
      <li><p>At vero eos et accusamus et iusto odio dignissimos ducimus qui blanditiis praesentium.</p><time>November 10th, 2012</time></li>
      <li><p>At vero eos et accusamus et iusto odio dignissimos ducimus qui blanditiis praesentium.</p><time>November 10th, 2012</time></li>
    </ul>
  </main>

  <footer class="site-footer">
    <div class="footer-nav">
      <a href="#">Home</a><span>|</span><a href="#">Trucks</a><span>|</span><a href="#">Services</a><span>|</span><a href="#">Parts</a><span>|</span><a href="#">About us</a><span>|</span><a href="#">Contact us</a><span>|</span><a href="#">Help</a>
    </div>
    <div class="copyright">Copyright © 2012 &nbsp;www.haulwrightfarmingdale.com &nbsp;All rights reserved.</div>
    <div class="social-badge"></div>
  </footer>
</body>
</html>
```